Quorvex clinic business card - double sided for young clinic

I require business cards for my aesthetic clinic specialising in the below treatments. I would like the cards to be modern as my clinic base are young 22-35 years old. I require my logo on it and would like the edges to be rounded.

I have an aesthetic clinic specialising in :
Quorvex
Lip Enhancement
Chemical Peels
Facial Fillers
Non Surgical Face Lift

I would the cards to have the following information on them:
My logo - (in grey/silver)
address
Phone number
services

Colours :
White/grey/silver and red

a nice image on there, perhaps a set of lips as this is a main service i deliver

Company Name: PDA Address: 52 Farrowmere Road, 4 Brackwell High Street, KT9 4WQ Phone: 0208 794 2160 Website: www.penningtondoweaesthetics.co.uk

Target Market(s)

clinics 22-45 years old mainly female

Industry/Entity Type

Business

Contact Information for Business Card

as above

Requirements
Must have
• logo
• Address
• Email
• Phone number
• Services i offer
Nice to have
• images

```html
<!DOCTYPE html>
<html lang="en">
<head>
<meta charset="utf-8">
<title>Pennington Dowe Aesthetics – Business Card</title>
<link href="https://fonts.googleapis.com/css2?family=Cinzel:wght@400&family=Mulish:wght@400;700&display=swap" rel="stylesheet">
<style>
  :root {
    --backdrop: #ecebe8;
    --card-front: #ebebeb;
    --card-back: #9b9c9e;
    --band: #a4a5a8;
    --ink: #5a5a5c;
    --ink-strong: #4e4e50;
    --silver: #c9c9cb;
    --silver-light: #e2e2e3;
    --lip-red: #d61f26;
    --lip-red-deep: #b5161c;
  }
  * { margin: 0; padding: 0; box-sizing: border-box; }
  html, body { width: 1200px; height: 1000px; overflow: hidden; }
  body { background: var(--backdrop); position: relative; font-family: "Mulish", sans-serif; }

  .card {
    position: absolute; left: 265px; width: 665px; height: 397px;
    border-radius: 22px; overflow: hidden;
    box-shadow: 0 4px 14px rgba(0,0,0,0.18);
  }
  .card--front { top: 73px; background: var(--card-front); }
  .card--back { top: 532px; background: var(--card-back); }

  .front-band { position: absolute; left: 0; bottom: 0; width: 665px; height: 40px; }

  .brand-mark {
    position: absolute; border-radius: 50%;
    background: radial-gradient(circle at 40% 35%, var(--silver-light), var(--silver));
  }
  .card--front .brand-mark { left: 108px; top: 36px; width: 90px; height: 90px; }
  .card--back .brand-mark { left: 285px; top: 98px; width: 96px; height: 96px; }

  .brand-name {
    position: absolute; font-family: "Cinzel", serif; font-weight: 400;
    line-height: 1; white-space: nowrap;
  }
  .brand-name__top { display: block; font-size: 23px; letter-spacing: 2.6px; }
  .brand-name__bottom { display: block; font-size: 33px; letter-spacing: 2.4px; margin-top: 4px; }
  .card--front .brand-name { left: 33px; top: 167px; color: var(--ink); }
  .card--back .brand-name { left: 0; width: 665px; top: 258px; text-align: center; color: var(--silver-light); }

  .contact { position: absolute; left: 33px; top: 272px; color: var(--ink); font-size: 16px; line-height: 22px; }
  .contact__lines { margin-top: 12px; }
  .contact__row { display: flex; align-items: center; gap: 8px; }
  .contact__row svg { width: 15px; height: 15px; fill: none; stroke: var(--ink); stroke-width: 1.6; }

  .lips-art {
    position: absolute; left: 442px; top: 76px; width: 152px; height: 94px;
    border-radius: 48px;
    background: radial-gradient(ellipse at 45% 55%, var(--lip-red), var(--lip-red-deep));
  }

  .services { position: absolute; left: 426px; top: 215px; color: var(--ink); }
  .services__title { font-weight: 700; font-size: 15px; color: var(--ink-strong); letter-spacing: 0.2px; margin-bottom: 7px; }
  .services__list { list-style: none; font-size: 16px; line-height: 22px; }
  .services__item { display: flex; align-items: center; gap: 8px; }
  .services__item svg { width: 12px; height: 12px; fill: none; stroke: var(--ink); stroke-width: 1.5; }
</style>
</head>
<body>

<section class="card card--front">
  <svg class="front-band" viewBox="0 0 665 40" preserveAspectRatio="none" aria-hidden="true">
    <path d="M0 40 L0 22 L325 22 C355 22 360 5 390 5 L665 5 L665 40 Z" fill="var(--band)"/>
  </svg>

  <div class="brand-mark" aria-hidden="true"></div>
  <div class="brand-name">
    <span class="brand-name__top">PENNINGTON DOWE</span>
    <span class="brand-name__bottom">AESTHETICS</span>
  </div>

  <div class="contact">
    <p>52 Farrowmere Road, 4 Brackwell<br>High Street, KT9 4WQ</p>
    <div class="contact__lines">
      <p class="contact__row">
        <svg viewBox="0 0 16 16"><path d="M2 6 C2 3 14 3 14 6 L11 7 L10 5 L6 5 L5 7 Z M4 9 L12 9 L13 13 L3 13 Z" fill="var(--ink)" stroke="none"/></svg>
        0208 794 2160
      </p>
      <p class="contact__row">
        <svg viewBox="0 0 16 16"><rect x="1.5" y="2.5" width="13" height="9"/><path d="M5 14 L11 14 M8 11.5 L8 14"/></svg>
        www.penningtondoweaesthetics.co.uk
      </p>
    </div>
  </div>

  <div class="lips-art" role="img" aria-label="Illustration of three sets of red lips"></div>

  <div class="services">
    <h2 class="services__title">SPECIALISING IN:</h2>
    <ul class="services__list">
      <li class="services__item"><svg viewBox="0 0 12 12"><rect x="0.75" y="0.75" width="10.5" height="10.5"/><path d="M3 6 L5 8.5 L10 2"/></svg>Quorvex</li>
      <li class="services__item"><svg viewBox="0 0 12 12"><rect x="0.75" y="0.75" width="10.5" height="10.5"/><path d="M3 6 L5 8.5 L10 2"/></svg>Lip Enhancement</li>
      <li class="services__item"><svg viewBox="0 0 12 12"><rect x="0.75" y="0.75" width="10.5" height="10.5"/><path d="M3 6 L5 8.5 L10 2"/></svg>Chemical Peels</li>
      <li class="services__item"><svg viewBox="0 0 12 12"><rect x="0.75" y="0.75" width="10.5" height="10.5"/><path d="M3 6 L5 8.5 L10 2"/></svg>Facial Fillers</li>
      <li class="services__item"><svg viewBox="0 0 12 12"><rect x="0.75" y="0.75" width="10.5" height="10.5"/><path d="M3 6 L5 8.5 L10 2"/></svg>Non Surgical Face Lift</li>
    </ul>
  </div>
</section>

<section class="card card--back">
  <div class="brand-mark" aria-hidden="true"></div>
  <div class="brand-name">
    <span class="brand-name__top">PENNINGTON DOWE</span>
    <span class="brand-name__bottom">AESTHETICS</span>
  </div>
</section>

</body>
</html>
```